Suds Harbor Laundromat Wordpress Design

We need a Wordpress website design for our laundromat, Suds Harbor Atlanta, at www.sudsharboratlanta-example.com. We would like to have 6 pages: Home, About Us, Services, Locations, Reviews and Contact us. We will provide content for the text on each page. What we do: We are a full service laundromat that provides dry cleaning drop off, professional laundry services, wash dry fold and self service laundry to the local community. We would like to use the color scheme from our logo to convey a warm, safe, and bright business that caters to its diverse community.
Updates

I like the structure of this laundromat website: http://www.tumblewashhub-example.com/ Using my logo and color scheme in the above referenced website is what. Am looking for. The photos attached to the project with the female model should be used as a primary focus and supplemented by actual photos of the equipment.

Target Market(s)

Our target market is a diverse group of people from Midtown Atlanta - LGBTQ community /Locals/Regulars that have been coming to laundromat for 30 years.

Industry/Entity Type

Laundromat

Coding

Coded - Design and coding required

Number of Pages Required

5+ page

Font styles to use
Sans Serif

Colors
0054AA
0677BA
7BADD7
CADEEF
E8F1F8

Requirements
Must have
• Feature this video on the main page: https://video.example.com/Qx7mBr2Lp0Z

```html
<!DOCTYPE html>
<html lang="en">
<head>
<meta charset="utf-8">
<title>Suds Harbor Atlanta</title>
<link href="https://fonts.googleapis.com/css2?family=Oswald:wght@300;400&family=Poppins:wght@400;500;600&family=Roboto+Slab:wght@800&display=swap" rel="stylesheet">
<style>
:root{
  --navy:#0054aa;
  --blue:#0677ba;
  --sky:#2aa8e0;
  --bright:#3db8ea;
  --soft:#7badd7;
  --pale:#cadeef;
  --mist:#e8f1f8;
  --ink:#333a44;
  --white:#ffffff;
}
*{margin:0;padding:0;box-sizing:border-box}
html,body{width:1200px;height:4149px;overflow:hidden}
body{position:relative;background:var(--white);font-family:'Poppins',sans-serif;color:var(--ink)}
.abs{position:absolute}
.cond{font-family:'Oswald',sans-serif;font-weight:400}

/* header */
.brand{left:60px;top:18px;width:160px}
.brand-name{font-family:'Oswald',sans-serif;font-size:28px;line-height:30px;color:var(--navy);display:flex;align-items:center;gap:7px}
.brand-name i{width:12px;height:12px;border-radius:50%;background:var(--sky);display:inline-block}
.brand-tag{font-size:7px;letter-spacing:.5px;color:var(--sky);margin-left:19px}
.call{left:928px;top:14px;display:flex;align-items:center;gap:8px;color:var(--white);font-size:12px}
.call .lbl{color:var(--sky)}
.call .ph{width:32px;height:32px;border-radius:50%;background:var(--navy);display:flex;align-items:center;justify-content:center}
.call .num{font-family:'Oswald',sans-serif;font-size:19px;color:var(--white)}
.nav{left:712px;top:52px;display:flex;gap:20px;font-size:12px;color:var(--white);align-items:center}
.nav .on{border:1px solid var(--white);border-radius:16px;padding:6px 16px}

/* hero */
.hero-art{left:0;top:0;width:1200px;height:680px}
.hero-title{left:60px;top:232px;font-family:'Roboto Slab',serif;font-weight:800;font-size:58px;line-height:56px;color:var(--navy)}
.hero-title span{color:var(--sky)}
.hero-text{left:61px;top:412px;width:400px;font-size:13px;line-height:22px;color:var(--ink)}
.btn{background:var(--blue);color:var(--white);border-radius:22px;font-family:'Oswald',sans-serif;font-size:16px;display:flex;align-items:center;justify-content:center}
.hero-btn{left:60px;top:491px;width:123px;height:38px}
.dots{left:60px;top:590px;display:flex;gap:6px}
.dots b{width:10px;height:10px;border:1px solid var(--blue);border-radius:50%}
.dots b.on{background:var(--blue)}
.scroll{left:590px;top:658px}

/* about */
.about-photo{left:139px;top:778px;width:314px;height:438px;border-radius:14px;background:linear-gradient(160deg,#9aa5a4,#e6e9ea 55%,#c9cfd2)}
.years{left:430px;top:820px;width:100px;height:100px;border-radius:50%;background:var(--white);box-shadow:0 4px 14px rgba(0,0,0,.12);text-align:center;color:var(--blue)}
.years b{display:block;font-family:'Oswald',sans-serif;font-weight:400;font-size:44px;line-height:50px;margin-top:12px}
.years span{font-family:'Oswald',sans-serif;font-size:17px}
.about-small{left:367px;top:1075px;width:184px;height:227px;border-radius:12px;background:var(--white);box-shadow:0 4px 14px rgba(0,0,0,.12);padding:12px}
.about-small div{width:100%;height:100%;border-radius:6px;background:linear-gradient(170deg,#c7ccd4,#8fb6da 45%,#eef0f2)}
.eyebrow{font-size:14px;color:var(--sky)}
.h2{font-family:'Oswald',sans-serif;font-weight:400;color:var(--blue);font-size:34px;line-height:40px}
.body{font-size:12.5px;line-height:20px;color:#555}
.about-eyebrow{left:668px;top:818px}
.about-title{left:667px;top:846px}
.about-text{left:672px;top:896px;width:400px}
.ticks{left:674px;top:980px;list-style:none;font-size:11.5px;color:#444}
.ticks li{display:flex;align-items:center;gap:16px;height:27px}
.learn{left:675px;top:1189px;width:124px;height:39px}

/* services */
.svc-bg{left:0;top:1382px;width:1200px;height:697px}
.svc-title{left:0;width:1200px;top:1460px;text-align:center;color:var(--white);font-size:33px}
.svc-sub{left:0;width:1200px;top:1510px;text-align:center;color:var(--sky);font-size:13px}
.svc-center{left:424px;top:1619px;width:344px;height:344px;border-radius:50%;background:linear-gradient(180deg,#cfe4ea,#7fa8c9 50%,#d9dcde);border:3px solid var(--white)}
.svc-icon{width:80px;height:80px;border-radius:50%;background:var(--sky);border:4px solid rgba(255,255,255,.35);display:flex;align-items:center;justify-content:center}
.svc-h{font-family:'Oswald',sans-serif;font-size:17px;color:var(--sky)}
.svc-p{font-size:11.5px;line-height:19.5px;color:var(--white);width:230px}
.left{text-align:right}

/* benefits */
.benefit-photo{left:113px;top:2159px;width:394px;height:464px;background:radial-gradient(ellipse at 55% 35%,#b5592f 0,#c77b4c 22%,#fff 48%),linear-gradient(180deg,transparent 60%,#1f63b8 60%);border-radius:0}
.video{left:644px;top:2315px;width:402px;height:226px;background:linear-gradient(135deg,#b12ee0,#ff3d9a 55%,#ff5a3a)}
.video .top{position:absolute;left:0;top:0;width:100%;height:28px;background:rgba(0,0,0,.55);color:var(--white);font-size:8px;padding:9px 8px}
.video .bar{position:absolute;left:0;bottom:0;width:100%;height:26px;background:#111}
.video .bar i{position:absolute;left:6px;right:6px;top:4px;height:2px;background:#666}
.video .bar i:before{content:"";position:absolute;left:0;width:20%;height:2px;background:#e00}

/* testimonials */
.testi-bg{left:0;top:2623px;width:1200px;height:486px;background:linear-gradient(90deg,#2a9bd8,var(--bright))}
.testi-title{left:0;width:1200px;top:2688px;text-align:center;color:var(--blue);font-size:34px}
.testi-sub{left:0;width:1200px;top:2737px;text-align:center;color:var(--white);font-size:13px}
.avatar{border-radius:50%;border:3px solid var(--white);background:linear-gradient(160deg,#e8c3a8,#b57b5e)}
.dot{border-radius:50%;background:#1f5ea8}
.quote{left:669px;top:2842px;width:390px;font-size:12.5px;line-height:22.5px;color:var(--white)}
.client{left:669px;top:2978px;color:var(--white);font-size:16px;display:flex;align-items:center;gap:10px}
.client:before{content:"";width:18px;height:2px;background:var(--white)}

/* contact */
.contact-title{left:0;width:1200px;top:3176px;text-align:center;color:var(--blue);font-size:34px}
.contact-sub{left:0;width:1200px;top:3224px;text-align:center;color:var(--sky);font-size:14px}
.contact-photo{left:562px;top:3282px;width:486px;height:486px;border-radius:50%;background:radial-gradient(circle at 60% 50%,#e9d27a,#7d6b3a 45%,#1d2544 75%)}
.form{left:177px;top:3351px;width:561px;height:330px;background:var(--white);box-shadow:0 0 22px rgba(0,0,0,.1)}
.field{left:54px;width:434px;border:1px solid #eee;border-radius:8px;font-size:10px;color:#777;padding:10px 14px}
.submit{left:53px;top:243px;width:105px;height:40px}

/* footer */
.foot{left:0;top:3780px;width:1200px;height:369px}
.f-brand{left:66px;top:3905px;font-family:'Oswald',sans-serif;font-size:40px;color:var(--white);display:flex;align-items:center;gap:10px}
.f-brand i{width:16px;height:16px;border-radius:50%;background:var(--white);display:inline-block}
.f-tag{left:136px;top:3960px;font-size:10px;color:var(--sky)}
.social{left:114px;top:4004px;display:flex;gap:11px}
.social b{width:40px;height:40px;border-radius:50%;background:var(--white);border:3px solid var(--pale)}
.f-h{font-family:'Oswald',sans-serif;font-size:16px;color:var(--white)}
.f-list{list-style:none;font-size:11.5px;color:var(--white)}
.f-list li{height:24px;display:flex;align-items:center;gap:16px}
.f-list li:before{content:"";width:5px;height:5px;border-radius:50%;background:var(--sky)}
.f-icon{width:38px;height:38px;border-radius:50%;background:var(--sky);display:flex;align-items:center;justify-content:center}
.copy{left:0;top:4108px;width:1200px;height:41px;background:var(--sky);color:var(--white);font-size:10.5px;text-align:center;line-height:41px}
</style>
</head>
<body>

<!-- hero art -->
<svg class="abs hero-art" viewBox="0 0 1200 680" aria-hidden="true">
  <circle cx="870" cy="287" r="372" fill="var(--navy)"/>
</svg>
<div class="abs" role="img" aria-label="Model in a blue dress walking past a row of washing machines" style="left:580px;top:-113px;width:774px;height:774px;border-radius:50%;background:linear-gradient(120deg,#b9dce4,#8fa4ae 40%,#2e6fc4 52%,#c6ccd0 64%,#8b8f92)"></div>

<header>
  <div class="abs brand">
    <div class="brand-name"><i></i>SUDS HARBOR</div>
    <div class="brand-tag">A FULL SERVICE LAUNDROMAT</div>
  </div>
  <div class="abs call">
    <span class="lbl">Call Us On :</span>
    <span class="ph"><svg width="16" height="16" viewBox="0 0 24 24"><path fill="#fff" d="M6.6 10.8a15 15 0 0 0 6.6 6.6l2.2-2.2c.3-.3.7-.4 1-.2 1.1.4 2.3.6 3.6.6.6 0 1 .4 1 1V20c0 .6-.4 1-1 1A17 17 0 0 1 3 4c0-.6.4-1 1-1h3.5c.6 0 1 .4 1 1 0 1.3.2 2.5.6 3.6.1.3 0 .7-.2 1z"/></svg></span>
    <span class="num">(404) 555 0182</span>
  </div>
  <nav class="abs nav">
    <span class="on">Home</span><span>About Us</span><span>Services</span><span>Locations</span><span>Reviews</span><span>Contact Us</span>
  </nav>
</header>

<section class="hero">
  <h1 class="abs hero-title">THE<br><span>SUDS</span><br>HARBOR</h1>
  <p class="abs hero-text">We Are A Full Service Laundromat That Provides Dry Cleaning Drop Off, Professional Laundry Services, Wash Dry Fold And Self Service Laundry To The Local Community</p>
  <div class="abs btn hero-btn">CONTACT US</div>
  <div class="abs dots"><b></b><b></b><b class="on"></b><b></b><b></b></div>
  <svg class="abs scroll" width="20" height="60" viewBox="0 0 20 60" aria-hidden="true"><path d="M10 0V58M3 50l7 8 7-8" stroke="#b7bcc4" fill="none"/></svg>
</section>

<section class="about">
  <div class="abs about-photo" role="img" aria-label="Row of front-loading washers with plants above"></div>
  <div class="abs years"><b>45</b><span>YEAR</span></div>
  <div class="abs about-small"><div role="img" aria-label="Attendant holding a stack of folded towels"></div></div>
  <div class="abs eyebrow about-eyebrow">Welcome To</div>
  <h2 class="abs h2 about-title">THE SUDS HARBOR</h2>
  <p class="abs body about-text">Lorem Ipsum has been the industry's standard dummy text ever since thes, when an unknown printer took a galley of type and scrambled it to make a type specimen book.</p>
  <ul class="abs ticks">
    <li><svg width="14" height="14"><circle cx="7" cy="7" r="5.5" fill="none" stroke="var(--sky)" stroke-width="2" stroke-dasharray="26 9"/></svg>In Business over 45 years</li>
    <li><svg width="14" height="14"><circle cx="7" cy="7" r="5.5" fill="none" stroke="var(--sky)" stroke-width="2" stroke-dasharray="26 9"/></svg>Voted "BEST COIN LAUNDRY" - Multiple years</li>
    <li><svg width="14" height="14"><circle cx="7" cy="7" r="5.5" fill="none" stroke="var(--sky)" stroke-width="2" stroke-dasharray="26 9"/></svg>One of Atlanta's First, Finest, &amp; Friendliest Coin Laundries</li>
    <li><svg width="14" height="14"><circle cx="7" cy="7" r="5.5" fill="none" stroke="var(--sky)" stroke-width="2" stroke-dasharray="26 9"/></svg>The best Wash-Dry-Fold in town</li>
    <li><svg width="14" height="14"><circle cx="7" cy="7" r="5.5" fill="none" stroke="var(--sky)" stroke-width="2" stroke-dasharray="26 9"/></svg>Cool - Comfortable - Clean</li>
    <li><svg width="14" height="14"><circle cx="7" cy="7" r="5.5" fill="none" stroke="var(--sky)" stroke-width="2" stroke-dasharray="26 9"/></svg>Over 50 well maintained machines</li>
    <li><svg width="14" height="14"><circle cx="7" cy="7" r="5.5" fill="none" stroke="var(--sky)" stroke-width="2" stroke-dasharray="26 9"/></svg>Commercial Accounts</li>
  </ul>
  <div class="abs btn learn">LEARN MORE</div>
</section>

<section class="services">
  <svg class="abs svc-bg" viewBox="0 0 1200 697" preserveAspectRatio="none" role="img" aria-label="Blue dome panel over a faint laundromat scene">
    <defs><linearGradient id="svcFill" x1="0" y1="0" x2="1" y2="1"><stop offset="0" stop-color="#1f6fc0"/><stop offset="1" stop-color="#0e58a8"/></linearGradient></defs>
    <path d="M0 250C170 60 390 0 600 0C640 0 660 2 680 4C460 10 220 90 0 300Z" fill="var(--sky)"/>
    <path d="M0 300C220 90 420 12 640 12C880 12 1090 150 1200 260V697H0Z" fill="url(#svcFill)"/>
  </svg>
  <h2 class="abs cond svc-title">SERVICES WE PROVIDE</h2>
  <p class="abs svc-sub">One of Atlanta's First, Finest, &amp; Friendliest Coin Laundries</p>
  <div class="abs svc-center" role="img" aria-label="Model in blue dress walking past washers"></div>

  <div class="abs svc-icon" style="left:342px;top:1629px"><svg width="38" height="38" viewBox="0 0 24 24" fill="none" stroke="#fff" stroke-width="1.3"><path d="M5 4h14v17H5zM9 4l3 4 3-4M12 8v13"/></svg></div>
  <div class="abs svc-icon" style="left:769px;top:1627px"><svg width="38" height="38" viewBox="0 0 24 24" fill="none" stroke="#fff" stroke-width="1.3"><rect x="6" y="3" width="12" height="18" rx="2"/><circle cx="12" cy="13" r="4"/></svg></div>
  <div class="abs svc-icon" style="left:345px;top:1882px"><svg width="38" height="38" viewBox="0 0 24 24" fill="none" stroke="#fff" stroke-width="1.3"><rect x="4" y="3" width="16" height="18" rx="2"/><circle cx="12" cy="13" r="5"/><path d="M7 6h3"/></svg></div>
  <div class="abs svc-icon" style="left:764px;top:1882px"><svg width="38" height="38" viewBox="0 0 24 24" fill="none" stroke="#fff" stroke-width="1.3"><rect x="3" y="5" width="18" height="14" rx="2"/><circle cx="12" cy="12" r="4"/></svg></div>

  <h3 class="abs svc-h left" style="left:95px;width:230px;top:1622px">DRY CLEANING DROP OFF</h3>
  <p class="abs svc-p left" style="left:95px;top:1656px">Lorem Ipsum has been the industry's standard dummy text ever since thes, when an unknown.</p>
  <h3 class="abs svc-h" style="left:873px;top:1622px">WASH DRY FOLD</h3>
  <p class="abs svc-p" style="left:873px;top:1656px">Lorem Ipsum has been the industry's standard dummy text ever since thes, when an unknown.</p>
  <h3 class="abs svc-h left" style="left:95px;width:230px;top:1875px">PROFESSIONAL LAUNDRY</h3>
  <p class="abs svc-p left" style="left:95px;top:1908px">Lorem Ipsum has been the industry's standard dummy text ever since thes, when an unknown.</p>
  <h3 class="abs svc-h" style="left:873px;top:1875px">SELF SERVICE LAUNDRY</h3>
  <p class="abs svc-p" style="left:873px;top:1908px">Lorem Ipsum has been the industry's standard dummy text ever since thes, when an unknown.</p>
</section>

<section class="benefits">
  <div class="abs benefit-photo" role="img" aria-label="Red-haired model in a blue dress, seen in profile"></div>
  <div class="abs eyebrow" style="left:644px;top:2152px">Why Choose Us</div>
  <h2 class="abs h2" style="left:644px;top:2178px">OUR LAUNDRY BENEFITS</h2>
  <p class="abs body" style="left:644px;top:2232px;width:400px">Lorem Ipsum has been the industry's standard dummy text ever since thes, when an unknown printer took a galley of type and scrambled it to make a type specimen book.</p>
  <div class="abs video" role="img" aria-label="Embedded music video player">
    <div class="top">Neon Harbor - Spin Cycle (Official Video)</div>
    <div class="bar"><i></i></div>
  </div>
</section>

<section class="testimonials">
  <div class="abs testi-bg" role="img" aria-label="Faint laundromat scene in bright blue"></div>
  <h2 class="abs cond testi-title">TESTIMONIALS</h2>
  <p class="abs testi-sub">What Our Client Say About THE SUDS HARBOR</p>
  <div class="abs avatar" role="img" aria-label="Client portrait" style="left:298px;top:2789px;width:70px;height:70px"></div>
  <div class="abs avatar" role="img" aria-label="Client portrait" style="left:153px;top:2866px;width:58px;height:58px"></div>
  <div class="abs avatar" role="img" aria-label="Client portrait" style="left:258px;top:2929px;width:80px;height:80px"></div>
  <div class="abs avatar" role="img" aria-label="Featured client portrait" style="left:385px;top:2840px;width:138px;height:138px"></div>
  <div class="abs dot" style="left:376px;top:2827px;width:48px;height:48px"></div>
  <div class="abs dot" style="left:382px;top:2993px;width:58px;height:58px"></div>
  <div class="abs" style="left:524px;top:2893px;width:107px;height:1px;background:rgba(255,255,255,.6)"></div>
  <p class="abs quote">" Lorem Ipsum has been the industry's standard dummy text ever since thes, when an unknown printer took a galley of type and scrambled it to make a type book Lorem Ipsum has been the industry's standard dummy text ever since thes, when an unknown Lorem Ipsum has been the industry's "</p>
  <div class="abs cond client">CLIENT NAME</div>
</section>

<section class="contact">
  <h2 class="abs cond contact-title">CONTACT US</h2>
  <p class="abs contact-sub">Have a question about our services?</p>
  <div class="abs contact-photo" role="img" aria-label="Laundromat storefront lit at night"></div>
  <form class="abs form">
    <div class="abs field" style="top:48px;height:36px">Name *</div>
    <div class="abs field" style="top:100px;height:37px">Email *</div>
    <div class="abs field" style="top:153px;height:76px">Message *</div>
    <div class="abs btn submit">SUBMIT</div>
  </form>
</section>

<footer>
  <svg class="abs foot" viewBox="0 0 1200 369" preserveAspectRatio="none" aria-hidden="true">
    <path d="M0 60C260 0 520 70 800 34C980 10 1110 6 1200 16V369H0Z" fill="var(--sky)"/>
    <path d="M0 74C260 18 520 86 800 48C980 24 1110 22 1200 30V369H0Z" fill="var(--navy)"/>
  </svg>
  <div class="abs f-brand"><i></i>SUDS HARBOR</div>
  <div class="abs f-tag">A FULL SERVICE LAUNDROMAT</div>
  <div class="abs social"><b></b><b></b><b></b></div>

  <h4 class="abs f-h" style="left:337px;top:3890px">SITEMAP</h4>
  <ul class="abs f-list" style="left:337px;top:3922px"><li>Home</li><li>About Us</li><li>Services</li><li>Locations</li><li>Reviews</li><li>Contact us</li></ul>

  <h4 class="abs f-h" style="left:612px;top:3890px">SERVICES</h4>
  <ul class="abs f-list" style="left:612px;top:3922px"><li>Dry Cleaning Drop Off</li><li>Professional Laundry</li><li>Wash Dry Fold</li><li>Self Service Laundry</li></ul>

  <h4 class="abs f-h" style="left:888px;top:3890px">CONTACT US</h4>
  <div class="abs f-icon" style="left:886px;top:3935px"><svg width="18" height="18" viewBox="0 0 24 24" fill="none" stroke="#fff" stroke-width="2"><path d="M12 22s7-7 7-12a7 7 0 0 0-14 0c0 5 7 12 7 12z"/><circle cx="12" cy="10" r="2.5"/></svg></div>
  <p class="abs" style="left:937px;top:3932px;width:200px;font-size:11.5px;line-height:20px;color:#fff">Brookview Plaza, 2270 Alder Row NE, # 112, Atlanta, GA 30309</p>
  <div class="abs f-icon" style="left:886px;top:4003px"><svg width="18" height="18" viewBox="0 0 24 24"><path fill="#fff" d="M6.6 10.8a15 15 0 0 0 6.6 6.6l2.2-2.2c.3-.3.7-.4 1-.2 1.1.4 2.3.6 3.6.6.6 0 1 .4 1 1V20c0 .6-.4 1-1 1A17 17 0 0 1 3 4c0-.6.4-1 1-1h3.5c.6 0 1 .4 1 1 0 1.3.2 2.5.6 3.6.1.3 0 .7-.2 1z"/></svg></div>
  <div class="abs" style="left:937px;top:4006px;font-size:17px;font-weight:600;color:#fff">(404) 555-0182</div>
  <div class="abs" style="left:940px;top:4034px;font-size:14px;color:#fff">Delivery Available</div>

  <div class="abs copy">©THE SUDS HARBOR - 2021 All rights reserved.</div>
</footer>

</body>
</html>
```